Personal Finance e-commerce website needs a simple budget design

Hello! I am starting to sell downloadable and printable budget planners, as shown in the attached file, for people to plan ahead on their personal finances. <br/><br/>I want to see a one-page design with similar columns (for example, "Expenses, Budget, and Actual"). I would also like to see the basic formula ("Net Income = Gross income - Total Expenses") somewhere on the design. Finally, I want the design to remain mostly minimalistic and simple for the average person to plan their personal monthly budgets.<br/><br/>However, other than that, the overall design, layout, and colors will be at the graphic designer's choice. If you have any questions for me, please let me know. Thank you for your time!

Industry/Entity Type

Financial Planning

Colors

Designer to choose colors to be used in the design.

Requirements
Must have
• I want to see a one-page design with similar columns (for example, "Expenses, Budget, and Actual").
• I want the design to remain mostly minimalistic and simple for the average person to plan their personal monthly budgets.
Nice to have
• I would also like to see the basic formula ("Net Income = Gross income - Total Expenses") somewhere on the design.

```html
<!DOCTYPE html>
<html lang="en">
<head>
<meta charset="UTF-8">
<title>Basic Monthly Budget</title>
<link href="https://fonts.googleapis.com/css2?family=Caprasimo&family=Lato:wght@400&display=swap" rel="stylesheet">
<style>
  :root {
    --backdrop: #dfebf2;
    --paper: #ffffff;
    --mint: #a3d5c6;
    --mint-pale: #e8f5f3;
    --rule: #3d3d3f;
    --ink: #1b1b1b;
    --cocoa: #5a4840;
    --on-dark: #ffffff;
    --texture-a: #f1f1f1;
    --texture-b: #fbfbfb;
  }
  * { margin: 0; padding: 0; box-sizing: border-box; }
  html, body { width: 1200px; height: 1200px; overflow: hidden; background: var(--backdrop); }
  .canvas { position: relative; width: 1200px; height: 1200px; }
  .sheet {
    position: absolute; left: 233px; top: 66px; width: 761px; height: 1067px;
    background: var(--paper); overflow: hidden;
  }
  .sheet-art { position: absolute; inset: 0; }
  .texture {
    position: absolute; left: 51px; top: 201px; width: 661px; height: 838px;
    background: linear-gradient(135deg, var(--texture-b) 0%, var(--texture-a) 40%, var(--texture-b) 70%, var(--texture-a) 100%);
    opacity: 0.7;
  }
  .title-band {
    position: absolute; left: 76px; top: 136px; width: 614px; height: 56px;
    background: var(--mint);
    display: flex; align-items: center; justify-content: center;
  }
  .title {
    font-family: "Caprasimo", "Cooper Black", serif;
    font-size: 47px; line-height: 1; color: var(--ink); letter-spacing: 0.5px;
  }
  .col-head {
    position: absolute; top: 240px; height: 22px;
    background: var(--ink); color: var(--on-dark);
    font-family: "Caprasimo", serif; font-size: 21px; line-height: 22px;
    text-align: center; white-space: nowrap;
  }
  .col-head.expense { left: 87px; width: 214px; }
  .col-head.budget { left: 344px; width: 156px; }
  .col-head.actual { left: 540px; width: 150px; }
  .col-hint {
    position: absolute; font-family: "Lato", sans-serif; font-size: 22px;
    line-height: 26px; color: var(--ink); text-align: center; white-space: nowrap;
  }
  .col-hint.expense { left: 81px; width: 200px; top: 317px; }
  .col-hint.budget { left: 314px; width: 200px; top: 310px; }
  .col-hint.actual { left: 507px; width: 200px; top: 310px; }
  .formula-pill {
    position: absolute; left: 95px; top: 997px; width: 605px; height: 59px;
    background: var(--cocoa); border-radius: 30px; color: var(--on-dark);
    font-family: "Lato", sans-serif;
  }
  .formula {
    position: absolute; left: 24px; top: 18px; font-size: 20px; line-height: 24px; white-space: nowrap;
  }
  .formula-notes {
    position: absolute; left: 448px; top: 14px; font-size: 7.5px; line-height: 11px; white-space: nowrap;
  }
</style>
</head>
<body>
<div class="canvas">
  <div class="sheet">
    <div class="texture" role="img" aria-label="Soft grey faceted diamond background pattern"></div>
    <svg class="sheet-art" width="761" height="1067" viewBox="0 0 761 1067">
      <circle cx="711" cy="-66" r="273" fill="var(--mint-pale)"/>
      <circle cx="82" cy="66" r="37" fill="var(--mint)"/>
      <circle cx="258" cy="66" r="25" fill="var(--mint-pale)"/>
      <circle cx="51" cy="1016" r="25" fill="var(--mint-pale)"/>
      <rect x="0" y="164" width="761" height="13" fill="var(--rule)"/>
      <g stroke="var(--ink)" stroke-width="1.3" stroke-dasharray="4.5 3.5" fill="none">
        <g id="row-lines">
          <line x1="94" x2="268" y1="412" y2="412"/><line x1="94" x2="268" y1="434.4" y2="434.4"/>
          <line x1="94" x2="268" y1="456.8" y2="456.8"/><line x1="94" x2="268" y1="479.2" y2="479.2"/>
          <line x1="94" x2="268" y1="501.6" y2="501.6"/><line x1="94" x2="268" y1="524" y2="524"/>
          <line x1="94" x2="268" y1="546.4" y2="546.4"/><line x1="94" x2="268" y1="568.8" y2="568.8"/>
          <line x1="94" x2="268" y1="591.2" y2="591.2"/><line x1="94" x2="268" y1="613.6" y2="613.6"/>
          <line x1="94" x2="268" y1="636" y2="636"/><line x1="94" x2="268" y1="658.4" y2="658.4"/>
          <line x1="94" x2="268" y1="680.8" y2="680.8"/><line x1="94" x2="268" y1="703.2" y2="703.2"/>
          <line x1="94" x2="268" y1="725.6" y2="725.6"/><line x1="94" x2="268" y1="748" y2="748"/>
          <line x1="94" x2="268" y1="770.4" y2="770.4"/><line x1="94" x2="268" y1="792.8" y2="792.8"/>
          <line x1="94" x2="268" y1="815.2" y2="815.2"/><line x1="94" x2="268" y1="837.6" y2="837.6"/>
          <line x1="94" x2="268" y1="860" y2="860"/><line x1="94" x2="268" y1="882.4" y2="882.4"/>
          <line x1="94" x2="268" y1="904.8" y2="904.8"/><line x1="94" x2="268" y1="927.2" y2="927.2"/>
          <line x1="94" x2="268" y1="949.6" y2="949.6"/><line x1="94" x2="268" y1="970" y2="970"/>
        </g>
        <use href="#row-lines" x="233"/>
        <use href="#row-lines" x="434"/>
      </g>
    </svg>

    <div class="title-band"><h1 class="title">Basic Monthly Budget</h1></div>

    <div class="col-head expense">Expense(category)</div>
    <div class="col-head budget">Budget(USD)</div>
    <div class="col-head actual">Actual(USD)</div>

    <p class="col-hint expense">Custom Category</p>
    <p class="col-hint budget">What you plan<br>to spend</p>
    <p class="col-hint actual">What&nbsp; you actually<br>spent</p>

    <div class="formula-pill">
      <p class="formula">Net Income = Gross income - Total Expenses</p>
      <p class="formula-notes">Net Income - how much money you kept<br>Gross Income - how much money you earned<br>Total Expenses- Actual Expenses</p>
    </div>
  </div>
</div>
</body>
</html>
```